I need a flyer designed in postcard size for a meditation class.

I want it to look arty and different.

The front should have a picture that depicts chocolate and meditation with the chocolate part being more eye catching. It should just read Velvet Stillness.

The back should have the details of the cousre. See the attached wrod doc.

anyone who loves chocolate

• a dark choclate theme but not too dark that it looks dreary. It should look peaceful and modern but elegant.

My logo should be displayed on the leaflet somewhere.
• Clear and uncluttered
• Cheesy cliched images. I want something original.

```html
<!DOCTYPE html>
<html lang="en">
<head>
<meta charset="utf-8">
<title>Velvet Stillness – Postcard Flyer</title>
<link rel="stylesheet" href="https://fonts.googleapis.com/css2?family=Sniglet:wght@400;800&family=Marcellus&family=Didact+Gothic&family=Archivo+Narrow:wght@400;500&display=swap">
<style>
  :root {
    --page: #ffffff;
    --cocoa-deep: #3a1c10;
    --cocoa-mid: #7a3f22;
    --cocoa-light: #b06a42;
    --panel: #873f1f;
    --panel-rule: #ffffff;
    --tan: #d7c49a;
    --cream: #ffffff;
    --glow-top: #e9dcb6;
    --glow-mid: #b9a27a;
    --glow-low: #6b5a45;
  }
  * { box-sizing: border-box; margin: 0; padding: 0; }
  html, body { width: 1200px; height: 794px; overflow: hidden; background: var(--page); }
  .canvas { position: relative; width: 1200px; height: 794px; background: var(--page); }

  .card { position: absolute; top: 14px; height: 754px; overflow: hidden; }
  .card--front { left: 42px; width: 522px; }
  .card--back { left: 634px; width: 518px; }

  .chocolate-shavings {
    position: absolute; inset: 0;
    background:
      radial-gradient(ellipse at 30% 20%, var(--cocoa-light) 0%, transparent 45%),
      radial-gradient(ellipse at 75% 65%, var(--cocoa-mid) 0%, transparent 50%),
      radial-gradient(ellipse at 20% 85%, var(--cocoa-light) 0%, transparent 40%),
      linear-gradient(160deg, var(--cocoa-mid), var(--cocoa-deep) 55%, var(--cocoa-mid));
  }

  /* Front */
  .hanger-tab {
    position: absolute; left: 208px; top: 0; width: 64px; height: 76px; background: var(--cream);
  }
  .meditation-scene {
    position: absolute; left: 60px; top: 58px; width: 384px; height: 384px; border-radius: 50%;
    border: 4px solid var(--cream);
    background: radial-gradient(circle at 50% 30%, var(--glow-top) 0%, var(--glow-mid) 45%, var(--glow-low) 100%);
  }
  .front-title { position: absolute; inset: 0; pointer-events: none; }
  .front-title svg { display: block; }
  .front-title .word-script { font-family: "Sniglet", system-ui, sans-serif; font-weight: 400; font-size: 60px; fill: var(--cream); }
  .front-title .word-caps { font-family: "Sniglet", system-ui, sans-serif; font-weight: 400; font-size: 62px; fill: var(--cream); }

  .brand-block {
    position: absolute; left: 214px; top: 578px; width: 82px; height: 176px; background: var(--cream);
    display: flex; flex-direction: column; align-items: center; justify-content: center; gap: 10px; padding: 8px;
  }
  .brand-block__mark { width: 42px; height: 42px; background: var(--panel); }
  .brand-block__name {
    font-family: "Didact Gothic", Arial, sans-serif; font-size: 11px; line-height: 1.25; color: var(--panel); text-align: center;
  }

  /* Back */
  .back-panel {
    position: absolute; left: 42px; top: 0; width: 438px; height: 754px; background: var(--panel);
    border-left: 3px solid var(--panel-rule); border-right: 3px solid var(--panel-rule);
    color: var(--cream); text-align: center;
  }
  .back-title { position: absolute; left: 0; top: 0; width: 432px; }
  .back-title svg { display: block; }
  .back-title .word-script { font-family: "Sniglet", system-ui, sans-serif; font-size: 56px; fill: var(--cream); }
  .back-title .word-caps { font-family: "Marcellus", Georgia, serif; font-size: 58px; fill: var(--tan); letter-spacing: 1px; }
  .back-title .word-course { font-family: "Sniglet", system-ui, sans-serif; font-size: 54px; fill: var(--cream); }

  .course-copy {
    position: absolute; left: 14px; right: 14px; top: 240px;
    font-family: "Didact Gothic", Arial, sans-serif; font-size: 13.6px; line-height: 18.4px; letter-spacing: 0.15px;
  }
  .course-copy h2 { font-weight: 400; font-size: 13.6px; text-transform: uppercase; }
  .course-copy section + section { margin-top: 18.4px; }
  .course-copy ul { list-style: none; }
  .course-copy li::before { content: "• "; }

  .contact {
    position: absolute; left: 0; right: 0; top: 694px;
    font-family: "Archivo Narrow", "Arial Narrow", sans-serif; font-size: 13px; line-height: 17px;
  }
</style>
</head>
<body>
<main class="canvas">

  <article class="card card--front">
    <div class="chocolate-shavings" role="img" aria-label="Close-up photograph of scattered curled dark chocolate shavings"></div>
    <div class="hanger-tab"></div>
    <div class="meditation-scene" role="img" aria-label="Silhouette of a person in a seated meditation pose, arms raised overhead, against a golden misty mountain range"></div>
    <div class="front-title">
      <svg width="522" height="754" viewBox="0 0 522 754">
        <defs><path id="front-arc" d="M92 446 Q 230 486 420 404"/></defs>
        <text class="word-script"><textPath href="#front-arc" startOffset="50%" text-anchor="middle">velvet</textPath></text>
        <text class="word-caps" x="254" y="562" text-anchor="middle" textLength="402" lengthAdjust="spacingAndGlyphs">STILLNESS</text>
      </svg>
    </div>
    <div class="brand-block">
      <span class="brand-block__mark"></span>
      <span class="brand-block__name">Clearwater Path Wellness</span>
    </div>
  </article>

  <article class="card card--back">
    <div class="chocolate-shavings" role="img" aria-label="Border strips of curled dark chocolate shavings"></div>
    <section class="back-panel">
      <div class="back-title">
        <svg width="432" height="230" viewBox="0 0 432 230">
          <defs><path id="back-arc" d="M86 92 Q 220 30 350 100"/></defs>
          <text class="word-script"><textPath href="#back-arc" startOffset="50%" text-anchor="middle">velvet</textPath></text>
          <text class="word-caps" x="216" y="150" text-anchor="middle">STILLNESS</text>
          <text class="word-course" x="216" y="210" text-anchor="middle">course</text>
        </svg>
      </div>

      <div class="course-copy">
        <section>
          <h2>Chocolate what?!</h2>
          <p>Yes you read right. Velvet Stillness! What could be better than combining the dilatable taste of chocolate with meditation, right? Well that is exactly what this course is all about with a little bit of Mindfulness thrown in.</p>
        </section>
        <section>
          <h2>Learn to eat chocolate without gaining weight!</h2>
          <p>“What do you mean? I already know how to eat Choco&shy;late.” We challenge you that you have in fact not really eaten chocolate. So we are going to teach you how to do it mindfully. This way you are guaranteed not to gain weight while eating chocolate.</p>
        </section>
        <section>
          <h2>What you get with the course:</h2>
          <ul>
            <li>A Velvet Stillness course book.</li>
            <li>Mindfulness and meditation instruction online.</li>
            <li>Learn how to eat chocolate mindfully.</li>
            <li>Learn Meditation techniques and postures.</li>
            <li>FREE mp3 Guided Meditation download.</li>
            <li>5% of the course goes to charity –</li>
          </ul>
          <p>Please see our website for this month’s charitable cause.</p>
        </section>
      </div>

      <footer class="contact">
        <p>www.velvet-stillness.com.au</p>
        <p>Brought to you by Clearwater Path Wellness</p>
        <p>Phone (02) 5550 1384</p>
      </footer>
    </section>
  </article>

</main>
</body>
</html>
```